Outdoor Company Business Card design

We are an outdoor adventure company needing a business card. We sell outdoor adventures and clothing. Please use our logo in the business card. We are looking for something unique but delivers a clear message as to who we are. Please be creative

Target Market(s)

Outdoor adventures

Industry/Entity Type

Business

Contact Information for Business Card

Business name: TrailBirch If using the logo, no need to have a spot for the name
Owner / CEO: Ross Dalby
Website: TrailBirch.example
Facebook: Social.example/TrailBirch
Instagram: @dalby_ross
phone number: 555-304-7192
Email: Dalbycrew@TrailBirch.example

Colors

Designer to choose colors to be used in the design.

Requirements
Must have
• The business card must include the details mentioned above. ie logo, my name, email, facebook, instagram, website, and phone number.
Should not have
• should not be cluttered or look messy

```html
<!DOCTYPE html>
<html lang="en">
<head>
<meta charset="utf-8">
<title>TrailBirch Business Card</title>
<link href="https://fonts.googleapis.com/css2?family=Lato:wght@400;700&display=swap" rel="stylesheet">
<style>
  :root {
    --brand-blue: #1e73be;
    --ink: #2b2f33;
    --paper: #ffffff;
    --backdrop: #e9ebee;
    --accent-pink: #e8528a;
  }
  * { margin: 0; padding: 0; box-sizing: border-box; }
  html, body { width: 1200px; height: 1200px; overflow: hidden; }
  body {
    background: var(--backdrop);
    font-family: "Lato", sans-serif;
    position: relative;
  }
  .card {
    position: absolute;
    left: 150px;
    width: 900px;
    height: 514px;
    box-shadow: 0 6px 24px rgba(0,0,0,0.15);
    overflow: hidden;
  }
  .card-front { top: 70px; background: var(--paper); }
  .card-back {
    top: 616px;
    background: var(--brand-blue);
    display: flex;
    align-items: center;
    justify-content: center;
  }
  .front-graphics { position: absolute; inset: 0; }
  .holder-name {
    position: absolute; left: 70px; top: 60px;
    font-size: 46px; font-weight: 400; color: var(--brand-blue);
    letter-spacing: 0.5px;
  }
  .holder-title {
    position: absolute; left: 72px; top: 122px;
    font-size: 22px; color: var(--ink);
  }
  .brand-name {
    position: absolute; right: 44px; top: 110px;
    font-size: 52px; font-weight: 700; color: var(--brand-blue);
    letter-spacing: 1px;
  }
  .band-website {
    position: absolute; right: 48px; top: 204px;
    font-size: 23px; color: var(--paper); letter-spacing: 0.5px;
  }
  .contact {
    position: absolute;
    display: flex; align-items: center; gap: 16px;
    font-size: 24px; color: var(--ink);
  }
  .contact-phone { left: 70px; top: 255px; }
  .contact-email { left: 70px; top: 305px; }
  .contact-page { left: 70px; top: 395px; }
  .contact-handle { left: 520px; top: 395px; }
  .icon { width: 30px; height: 30px; flex: none; }
  .page-dot {
    width: 30px; height: 30px; border-radius: 50%;
    background: var(--brand-blue); flex: none;
  }
  .handle-square {
    width: 30px; height: 30px; border-radius: 7px;
    background: var(--accent-pink); flex: none;
  }
  .back-brand {
    font-size: 96px; font-weight: 700; color: var(--paper);
    letter-spacing: 3px;
  }
</style>
</head>
<body>
  <section class="card card-front">
    <svg class="front-graphics" width="900" height="514" viewBox="0 0 900 514">
      <line x1="60" y1="190" x2="560" y2="190" stroke="var(--brand-blue)" stroke-width="2"/>
      <path d="M548,190 L900,190 L900,250 L585,250 Q566,250 558,232 Z" fill="var(--brand-blue)"/>
    </svg>
    <div class="holder-name">Ross Dalby</div>
    <div class="holder-title">CEO</div>
    <div class="brand-name">TrailBirch</div>
    <div class="band-website">TrailBirch.example</div>

    <div class="contact contact-phone">
      <svg class="icon" viewBox="0 0 30 30">
        <circle cx="15" cy="15" r="15" fill="var(--brand-blue)"/>
        <path d="M10.5 8.5c1-.6 1.7-.3 2.2.6l1 2c.4.8.2 1.4-.5 1.9l-.8.6c.7 1.6 1.8 2.8 3.4 3.6l.6-.8c.5-.7 1.1-.9 1.9-.5l2 1c.9.5 1.2 1.2.6 2.2-1 1.6-2.6 2.2-4.5 1.4-3.4-1.4-6-4-7.3-7.3-.8-1.9-.2-3.6 1.4-4.7z" fill="#fff"/>
      </svg>
      <span>555-304-7192</span>
    </div>
    <div class="contact contact-email">
      <svg class="icon" viewBox="0 0 30 30">
        <circle cx="15" cy="15" r="15" fill="var(--brand-blue)"/>
        <rect x="8" y="10" width="14" height="10" rx="1.5" fill="#fff"/>
        <path d="M8.5 10.8 L15 15.5 L21.5 10.8" fill="none" stroke="var(--brand-blue)" stroke-width="1.4"/>
      </svg>
      <span>Dalbycrew@TrailBirch.example</span>
    </div>
    <div class="contact contact-page">
      <span class="page-dot"></span>
      <span>Social.example/TrailBirch</span>
    </div>
    <div class="contact contact-handle">
      <span class="handle-square"></span>
      <span>@dalby_ross</span>
    </div>
  </section>

  <section class="card card-back">
    <div class="back-brand">TrailBirch</div>
  </section>
</body>
</html>
```